New Zealand Luggage Importer Needs Business Cards

We need professional, creative and fashionable business cards created.
We are based in New Zealand and import and distribute high-end, quality, fashionable and durable luggage.
We pride ourselves on selling the very best quality luggage, second only to 1 brand (which we won't mention here)...we use the same manufacturer. However, our prices are much more reasonable.
Industry/Entity Type
Business
Contact Information for Business Card
Mark Dunsley
027 512 4068
3/17 Harlow Street, Pinecrest Flats, Auckland, 0614
PO Box 204377, Fernside, Auckland 0731
09-528-3916
sales@brivancases.co.nz / www.brivancases.co.nz

```html
<!DOCTYPE html>
<html lang="en">
<head>
<meta charset="utf-8">
<title>Brivan Cases – Business Cards</title>
<link href="https://fonts.googleapis.com/css2?family=Montserrat:wght@500;700&family=Roboto+Slab:wght@700&display=swap" rel="stylesheet">
<style>
  :root {
    --bg: #e4e4e6;
    --olive-light: #56663f;
    --olive-dark: #2c3a1e;
    --olive-edge: #3a3820;
    --band-green: #3b5e35;
    --name-green: #2f5a2b;
    --ink: #1d1d1d;
    --paper: #ffffff;
    --case-dark: #2a2b2d;
    --case-light: #5a5c60;
  }
  * { box-sizing: border-box; margin: 0; padding: 0; }
  html, body { width: 1200px; height: 750px; overflow: hidden; }
  body {
    background: var(--bg);
    font-family: "Montserrat", sans-serif;
    position: relative;
  }
  .card {
    position: absolute;
    top: 225px;
    width: 520px;
    height: 300px;
    border-radius: 4px;
    overflow: hidden;
    box-shadow: 0 6px 18px rgba(0,0,0,0.12);
  }
  .card-back {
    left: 50px;
    background: linear-gradient(120deg, var(--olive-light) 0%, var(--olive-dark) 70%);
    border: 6px solid var(--olive-edge);
    display: flex;
    align-items: center;
    justify-content: center;
  }
  .brand-name {
    font-family: "Montserrat", sans-serif;
    font-weight: 700;
    letter-spacing: 2px;
    white-space: nowrap;
  }
  .card-back .brand-name { color: var(--paper); font-size: 34px; }
  .card-front {
    left: 630px;
    background: var(--paper);
  }
  .card-front .brand-name {
    position: absolute;
    left: 34px;
    top: 112px;
    color: var(--ink);
    font-size: 22px;
  }
  .product-photo {
    position: absolute;
    right: 26px;
    top: 18px;
    width: 220px;
    height: 150px;
    border-radius: 6px;
    background: linear-gradient(135deg, var(--case-light), var(--case-dark) 60%);
  }
  .holder-name {
    position: absolute;
    left: 34px;
    top: 150px;
    font-family: "Roboto Slab", serif;
    font-weight: 700;
    font-size: 26px;
    color: var(--name-green);
  }
  .contact-band {
    position: absolute;
    left: 0; right: 0; bottom: 0;
    height: 108px;
    background: var(--band-green);
    color: var(--paper);
    font-size: 10.5px;
    font-weight: 500;
    display: flex;
    justify-content: space-between;
    padding: 18px 24px 0 34px;
  }
  .contact-list { list-style: none; display: flex; flex-direction: column; gap: 9px; }
  .contact-list li { display: flex; align-items: center; gap: 8px; white-space: nowrap; }
  .contact-list svg { width: 13px; height: 13px; flex: none; }
  .address { display: flex; gap: 8px; align-items: flex-start; }
  .address p { line-height: 1.7; white-space: nowrap; }
</style>
</head>
<body>
  <section class="card card-back">
    <span class="brand-name">BRIVAN CASES</span>
  </section>

  <section class="card card-front">
    <div class="product-photo" role="img" aria-label="Photo of three black hard-shell suitcases"></div>
    <span class="brand-name">BRIVAN CASES</span>
    <h1 class="holder-name">Mark Dunsley</h1>

    <div class="contact-band">
      <ul class="contact-list">
        <li>
          <svg viewBox="0 0 24 24" aria-hidden="true"><path fill="#fff" d="M6.6 10.8a15 15 0 0 0 6.6 6.6l2.2-2.2a1 1 0 0 1 1-.25 11.4 11.4 0 0 0 3.6.57 1 1 0 0 1 1 1V20a1 1 0 0 1-1 1A17 17 0 0 1 3 4a1 1 0 0 1 1-1h3.5a1 1 0 0 1 1 1c0 1.25.2 2.45.57 3.57a1 1 0 0 1-.25 1z"/></svg>
          027 512 4068
        </li>
        <li>
          <svg viewBox="0 0 24 24" aria-hidden="true"><rect x="2" y="5" width="20" height="14" rx="2" fill="#fff"/><path d="M3 6l9 7 9-7" stroke="#3b5e35" stroke-width="2" fill="none"/></svg>
          sales@brivancases.co.nz
        </li>
        <li>
          <svg viewBox="0 0 24 24" aria-hidden="true"><circle cx="12" cy="12" r="10" fill="none" stroke="#fff" stroke-width="2"/><path d="M2 12h20M12 2c3 3 3 17 0 20M12 2c-3 3-3 17 0 20" stroke="#fff" stroke-width="1.6" fill="none"/></svg>
          www.brivancases.co.nz
        </li>
      </ul>
      <div class="address">
        <svg viewBox="0 0 24 24" width="13" height="13" aria-hidden="true"><path fill="#fff" d="M12 2a7 7 0 0 0-7 7c0 5 7 13 7 13s7-8 7-13a7 7 0 0 0-7-7zm0 9.5A2.5 2.5 0 1 1 12 6.5a2.5 2.5 0 0 1 0 5z"/></svg>
        <p>3/17 Harlow Street, Pinecrest Flats, Auckland, 0614<br>PO Box 204377, Fernside, Auckland 0731</p>
      </div>
    </div>
  </section>
</body>
</html>
```